・ターゲット
美容室は銀座にあり、客層は20代~50代の女性です。
メインターゲットは30代です。

・サイトの色
白がベースでブラック、グレーで洗練された
透明感を表現してください。

「シンプルで美しく、魅力的なデザインでかつ予約導線がよいサイト」
を目指しています。

ラフデザイン案がありますので、
レイアウトは基本的にラフデザインをベースにしていただき、
ユーザビリティ的によりよくなる提案があれば理由とともに
アレンジしてください。

ロゴ、使用素材はお渡しします。
1ページ
白、グレー、黒
• フォトショップ形式 (.psd)
• PNG形式 (.png)
提案数が想定よりも少ないため延長させていただきます。参加報酬も4件に増やさせていただきました。
たくさんのご応募ありがとうございます。
トップの表記では選定期限が1/31までとなっておりますが、
現在、最終選定期限を2/5になっております。

期限までには当選対象者にご連絡できるかと思いますのでよろしくお願いします。
現在、候補のランサー様に修正依頼を投げています。
最終選定期限を再度、延長していただいています。

長くなってしまい申し訳ございませんが今しばらくお待ちください。

素材の魅力を最大限に引き出していただけたところが、クライアントに気に入っていただけたポイントでした。ありがとうございます。

たくさんのご提案ありがとうございました。

言葉足らずの点もあったと思いますが、言語外の意図を読み取っていただけて、これほど多様なデザインの提案をいただけるとは思っていませんでした。

たくさんの中から絞り込むのはとても大変な作業で、時間もかかってしまい申し訳ありませんでした。お選びできなかった皆様に申し訳ない気持ちでいっぱいです。
また、このような機会がありましたら、何卒よろしくお願いいたします。

```html
<!DOCTYPE html>
<html lang="ja">
<head>
<meta charset="utf-8">
<title>Salon | Ginza Hair Salon</title>
<link href="https://fonts.googleapis.com/css2?family=Cormorant+Garamond:wght@400;500;600&family=Noto+Sans+JP:wght@400;500;700&family=Noto+Serif+JP:wght@400;600&display=swap" rel="stylesheet">
<style>
:root{
  --ink:#222;
  --text:#444;
  --muted:#8a8a8a;
  --line:#d6d6d6;
  --paper:#fff;
  --mist:#f3f3f3;
  --band:#3b3b3b;
  --band-dark:#2a2a2a;
  --accent:#c43a3a;
  --rose:#d0667a;
  --photo-a:#d9d4cf;
  --photo-b:#8d8580;
  --photo-c:#bfb7b0;
}
*{box-sizing:border-box;margin:0;padding:0}
html,body{width:1200px;height:3240px;overflow:hidden}
body{background:var(--paper);color:var(--text);font-family:"Noto Sans JP",sans-serif;font-size:14px;line-height:1.6;position:relative}
.serif{font-family:"Cormorant Garamond",serif}

/* Header */
.hero{position:absolute;left:0;top:0;width:1200px;height:620px;background:linear-gradient(90deg,#f6f6f6 0%,#ececec 30%,#fafafa 100%)}
.hero-photo{position:absolute;left:330px;top:0;width:870px;height:620px;background:linear-gradient(110deg,#e9e9e9 0%,#b9b5b2 35%,#6f6a67 55%,#d4d1ce 80%,#f2f2f2 100%)}
.brand{position:absolute;left:40px;top:40px;display:flex;flex-direction:column;align-items:flex-start;gap:18px}
.brand-mark{width:70px;height:70px;background:var(--band-dark)}
.brand-name{font-family:"Cormorant Garamond",serif;font-size:78px;font-weight:500;color:var(--ink);line-height:1}
.hero-title{position:absolute;left:40px;top:520px;font-family:"Cormorant Garamond",serif;font-size:28px;letter-spacing:3px;color:var(--ink);line-height:1.2}

/* Global nav */
.gnav{position:absolute;left:0;top:620px;width:1200px;height:80px;border-top:1px solid var(--line);border-bottom:1px solid var(--line);display:flex;align-items:stretch;background:var(--paper)}
.gnav-item{flex:1;display:flex;flex-direction:column;justify-content:center;align-items:center;border-right:1px solid var(--line);font-family:"Cormorant Garamond",serif;font-size:17px;font-weight:600;letter-spacing:1px;color:var(--ink)}
.gnav-item small{font-family:"Noto Sans JP",sans-serif;font-size:10px;font-weight:400;color:var(--muted);letter-spacing:0}
.gnav-item.is-current{background:var(--band-dark);color:#fff;flex:.7}
.gnav-item.is-current small{color:#ccc}
.gnav-item.is-reserve{color:var(--rose);flex:1.4}
.gnav-tel{flex:1.3;display:flex;flex-direction:column;justify-content:center;align-items:center;font-family:"Cormorant Garamond",serif;font-size:22px;font-weight:600;color:var(--accent)}
.gnav-tel small{font-size:10px;color:var(--muted);font-family:"Noto Sans JP",sans-serif}

/* Sections with side label */
.section{position:absolute;left:0;width:1200px}
.side-label{position:absolute;left:0;top:0;width:50px;height:100%;background:var(--band)}
.side-label span{position:absolute;left:50%;top:30px;transform:translateX(-50%) rotate(180deg);writing-mode:vertical-rl;font-family:"Cormorant Garamond",serif;font-weight:600;font-size:26px;letter-spacing:6px;color:#fff}
.section-body{position:absolute;left:70px;right:10px;top:0;bottom:0}

.catalog{top:710px;height:700px}
.catalog-grid{display:grid;grid-template-columns:repeat(4,1fr);gap:24px 20px;padding-top:20px}
.look-photo{height:240px;background:linear-gradient(160deg,var(--photo-a),var(--photo-b) 60%,var(--photo-c))}
.look-photo.warm{background:linear-gradient(160deg,#e6dfd7,#9b7c64 60%,#d8cdc2)}
.look-photo.cool{background:linear-gradient(160deg,#e4e4e4,#4a4644 60%,#cfcfcf)}
.look-caption{padding:8px 4px 0;font-size:11px;line-height:1.5;color:var(--text)}
.look-caption b{display:block;font-size:12px;color:var(--ink)}
.look-caption .tag{display:inline-block;margin-top:2px;padding:0 6px;border:1px solid var(--rose);color:var(--rose);font-size:10px}

.stylist{top:1425px;height:595px}
.stylist-grid{display:grid;grid-template-columns:repeat(5,1fr);gap:24px 16px;padding-top:20px}
.stylist-photo{height:200px;background:linear-gradient(170deg,#eeeeee,#a9a4a0 55%,#5e5a57)}
.stylist-name{text-align:center;padding-top:8px;font-family:"Noto Serif JP",serif;font-size:15px;color:var(--ink);line-height:1.3}
.stylist-name small{display:block;font-family:"Cormorant Garamond",serif;font-size:12px;color:var(--muted);letter-spacing:1px}

/* Welcome */
.welcome{top:2035px;height:430px;left:70px;width:1110px}
.welcome-head{display:flex;align-items:center;gap:12px;border-bottom:1px solid var(--line);padding-bottom:8px;font-family:"Noto Serif JP",serif;font-size:26px;color:var(--ink)}
.welcome-head i{width:14px;height:14px;background:var(--band)}
.welcome-row{display:flex;gap:28px;margin-top:18px;align-items:flex-start}
.welcome-photo{width:200px;height:100px;flex:none;background:linear-gradient(135deg,#f2f2f2,#a8a8a8 60%,#d9d9d9)}
.welcome-text{font-size:15px;line-height:1.8;color:var(--text)}
.welcome-deco{position:absolute;left:0;right:0;bottom:0;text-align:center;font-family:"Cormorant Garamond",serif;font-size:96px;color:#ececec;line-height:1}

/* Special */
.special{top:2470px;height:290px}
.special-cols{display:grid;grid-template-columns:1fr 1fr;gap:40px;padding-top:10px}
.news-head{display:flex;align-items:center;gap:10px;font-family:"Cormorant Garamond",serif;font-weight:600;font-size:26px;letter-spacing:1px;color:var(--ink);border-bottom:1px solid var(--line);padding-bottom:4px}
.news-head i{width:14px;height:14px;background:var(--muted)}
.news-head small{font-family:"Noto Sans JP",sans-serif;font-size:13px;color:var(--muted);font-weight:400}
.news-list{list-style:none;margin-top:10px;font-size:13px;line-height:1.55}
.news-list li{margin-bottom:6px}
.news-list time{color:var(--accent);margin-right:6px}

/* Banner row */
.banners{position:absolute;left:70px;top:2770px;width:1110px;height:110px;display:flex;gap:14px;align-items:stretch}
.banner{border:1px solid var(--line);display:flex;align-items:center;justify-content:center;gap:10px;font-size:14px;color:var(--ink);padding:0 14px}
.banner-open{width:110px;background:var(--accent);color:#fff;flex-direction:column;gap:0;font-family:"Cormorant Garamond",serif;font-size:36px;font-weight:600;line-height:1}
.banner-open small{font-size:18px;letter-spacing:2px}
.banner-circle{width:90px;border-radius:50%;border:none;background:var(--rose);color:#fff;font-size:13px;text-align:center;padding:0}
.banner-wide{flex:1}
.banner svg{flex:none}
.banner-dark{flex:1;background:var(--band);color:#fff;border:none;flex-direction:column;gap:0;font-family:"Cormorant Garamond",serif;font-size:24px;letter-spacing:2px}
.banner-dark small{font-family:"Noto Sans JP",sans-serif;font-size:12px;letter-spacing:0}
.banner-sns i{width:44px;height:44px;background:#4a4a4a}

/* Information */
.info{top:2900px;height:265px}
.info-cols{display:grid;grid-template-columns:1.1fr .9fr 1fr;gap:30px;padding-top:14px}
.info-name{font-family:"Cormorant Garamond",serif;font-size:32px;font-weight:600;color:var(--ink);line-height:1.1}
.info-addr{font-size:14px;line-height:1.8;margin-top:6px}
.info-tel{font-family:"Cormorant Garamond",serif;font-size:24px;font-weight:600;color:var(--ink)}
.info-note{font-size:11px;color:var(--muted);margin-top:6px;line-height:1.6}
.info-map{height:220px;background:linear-gradient(135deg,#efefef,#d2d2d2)}
.hours{width:100%;border-collapse:collapse;font-size:13px}
.hours th,.hours td{border-bottom:1px solid var(--line);padding:6px 4px;text-align:left;font-weight:400}
.hours th{color:var(--ink);width:40%}

/* Footer */
.footer{position:absolute;left:0;top:3175px;width:1200px;height:65px;background:var(--band-dark);color:#fff}
.fnav{display:flex;justify-content:space-between;padding:8px 30px 0;font-family:"Cormorant Garamond",serif;font-size:15px;font-weight:600;letter-spacing:1px}
.copy{text-align:center;font-size:11px;color:#bbb;margin-top:6px}
</style>
</head>
<body>

<header class="hero">
  <div class="hero-photo" role="img" aria-label="Monochrome portrait photograph of a model with soft wavy hair"></div>
  <div class="brand">
    <div class="brand-mark"></div>
    <div class="brand-name">Salon</div>
  </div>
  <p class="hero-title">2013A/W COLLECTION<br>HAIR CATALOG</p>
</header>

<nav class="gnav">
  <a class="gnav-item is-current">HOME<small>ホーム</small></a>
  <a class="gnav-item">INFORMATION/PRESS<small>ご案内/お知らせ</small></a>
  <a class="gnav-item">STYLIST<small>スタイリスト</small></a>
  <a class="gnav-item">CATALOG<small>カタログ</small></a>
  <a class="gnav-item">ACCESS<small>所在地</small></a>
  <a class="gnav-item">PRICE<small>料金</small></a>
  <a class="gnav-item">CONTACT<small>お問い合わせ</small></a>
  <a class="gnav-item">RECRUIT<small>採用情報</small></a>
  <a class="gnav-item is-reserve">RESERVATION/ご予約<small>ご予約はこちら</small></a>
  <div class="gnav-tel">03-5000-4127<small>ご予約・お問い合わせ</small></div>
</nav>

<section class="section catalog">
  <div class="side-label"><span>CATALOG</span></div>
  <div class="section-body">
    <div class="catalog-grid">
      <article><div class="look-photo warm" role="img" aria-label="Hair catalog photo: brown bob with soft waves"></div><div class="look-caption"><b>STYLIST 高森 美樹</b>ふんわり軽いボブスタイル<br><span class="tag">詳細・ご予約</span></div></article>
      <article><div class="look-photo cool" role="img" aria-label="Hair catalog photo: long dark straight hair"></div><div class="look-caption"><b>STYLIST 水野 さやか</b>艶のあるロングストレート<br><span class="tag">詳細・ご予約</span></div></article>
      <article><div class="look-photo" role="img" aria-label="Hair catalog photo: short bob with bangs"></div><div class="look-caption"><b>STYLIST 早瀬 健太</b>前髪ありの大人ショート<br><span class="tag">詳細・ご予約</span></div></article>
      <article><div class="look-photo warm" role="img" aria-label="Hair catalog photo: light blonde short cut"></div><div class="look-caption"><b>STYLIST 小野 真理</b>明るめカラーのショート<br><span class="tag">詳細・ご予約</span></div></article>
      <article><div class="look-photo cool" role="img" aria-label="Hair catalog photo: layered medium dark hair"></div><div class="look-caption"><b>STYLIST 高森 美樹</b>レイヤーで動くミディアム<br><span class="tag">詳細・ご予約</span></div></article>
      <article><div class="look-photo" role="img" aria-label="Hair catalog photo: black chin-length bob"></div><div class="look-caption"><b>STYLIST 水野 さやか</b>黒髪の上品なボブ<br><span class="tag">詳細・ご予約</span></div></article>
      <article><div class="look-photo warm" role="img" aria-label="Hair catalog photo: elegant updo"></div><div class="look-caption"><b>STYLIST 早瀬 健太</b>華やかなアップスタイル<br><span class="tag">詳細・ご予約</span></div></article>
      <article><div class="look-photo" role="img" aria-label="Hair catalog photo: long beige waves"></div><div class="look-caption"><b>STYLIST 小野 真理</b>ベージュの柔らかロング<br><span class="tag">詳細・ご予約</span></div></article>
    </div>
  </div>
</section>

<section class="section stylist">
  <div class="side-label"><span>STYLIST</span></div>
  <div class="section-body">
    <div class="stylist-grid">
      <div><div class="stylist-photo" role="img" aria-label="Stylist portrait photo"></div><p class="stylist-name">高森 美樹<small>MIKI TAKAMORI</small></p></div>
      <div><div class="stylist-photo" role="img" aria-label="Stylist portrait photo"></div><p class="stylist-name">水野 さやか<small>SAYAKA MIZUNO</small></p></div>
      <div><div class="stylist-photo" role="img" aria-label="Stylist portrait photo"></div><p class="stylist-name">早瀬 健太<small>KENTA HAYASE</small></p></div>
      <div><div class="stylist-photo" role="img" aria-label="Stylist portrait photo"></div><p class="stylist-name">小野 真理<small>MARI ONO</small></p></div>
      <div><div class="stylist-photo" role="img" aria-label="Stylist portrait photo"></div><p class="stylist-name">北川 亮介<small>RYOSUKE KITAGAWA</small></p></div>
      <div><div class="stylist-photo" role="img" aria-label="Stylist portrait photo"></div><p class="stylist-name">杉本 一平<small>IPPEI SUGIMOTO</small></p></div>
      <div><div class="stylist-photo" role="img" aria-label="Stylist portrait photo"></div><p class="stylist-name">松田 悠<small>YU MATSUDA</small></p></div>
      <div><div class="stylist-photo" role="img" aria-label="Stylist portrait photo"></div><p class="stylist-name">青木 大輔<small>DAISUKE AOKI</small></p></div>
      <div><div class="stylist-photo" role="img" aria-label="Stylist portrait photo"></div><p class="stylist-name">石原 トモコ<small>TOMOKO ISHIHARA</small></p></div>
      <div><div class="stylist-photo" role="img" aria-label="Stylist portrait photo"></div><p class="stylist-name">村上 翔<small>SHO MURAKAMI</small></p></div>
    </div>
  </div>
</section>

<section class="section welcome">
  <h2 class="welcome-head"><i></i>Salonへようこそ!</h2>
  <div class="welcome-row">
    <div class="welcome-photo" role="img" aria-label="Salon interior with styling chairs"></div>
    <p class="welcome-text">Salonの由来は、フランスの上流階級が集い語らう社交場「サロン」に由来しています。<br>ホテルのようなレセプション、白が基調のモダンなカットフロア。フルフラットベッドのシャンプーブースなどで構成された非日常な空間で、高度なカットテクニックとホスピタリティをご提供いたします。</p>
  </div>
  <div class="welcome-row">
    <div class="welcome-photo" role="img" aria-label="Shampoo area of the salon"></div>
    <p class="welcome-text">最新トレンドを常に意識しながらも、ゲストそれぞれのライフスタイルに合ったおしゃれをご提案してまいります。</p>
  </div>
  <div class="welcome-row">
    <div class="welcome-photo" role="img" aria-label="Salon reception lounge"></div>
    <p class="welcome-text">今までになく美容室を目指し、銀座にオープンしても年数となりました。これからもゲストの皆様が必ずして笑顔でお過ごしいただける、大人のための上質サロンを目指し、ゲストとスタッフが和やかに過ごす特別な空間をご提供してまいります。</p>
  </div>
  <p class="welcome-deco" aria-hidden="true">Salon</p>
</section>

<section class="section special">
  <div class="side-label"><span>SPECIAL</span></div>
  <div class="section-body">
    <div class="special-cols">
      <div>
        <h3 class="news-head"><i></i>RANKING<small>人気商品ランキング</small></h3>
        <ul class="news-list">
          <li><time>2014年1月6日</time>冬限定シャンプーランキング更新</li>
          <li><time>2014年1月10日</time>常連の皆様におすすめの人気トリートメント</li>
          <li><time>2014年1月18日</time>今月のスタイリング剤ランキング</li>
          <li><time>2014年1月24日</time>銀座店限定ヘアケアセットのご紹介</li>
          <li><time>2014年1月30日</time>春に向けたカラーケア人気商品</li>
        </ul>
      </div>
      <div>
        <h3 class="news-head"><i></i>MEDIA / PRESS / INFORMATION</h3>
        <ul class="news-list">
          <li><time>2014年1月6日</time>新年の営業についてのお知らせ</li>
          <li><time>2014年1月10日</time>女性誌にスタイルが掲載されました</li>
          <li><time>2014年1月18日</time>春の新メニューのご案内</li>
          <li><time>2014年1月24日</time>ヘアカタログ誌に当店が掲載されました</li>
          <li><time>2014年1月30日</time>2月の定休日のお知らせ</li>
        </ul>
      </div>
    </div>
  </div>
</section>

<div class="banners">
  <div class="banner banner-open">24h<small>OPEN</small></div>
  <div class="banner banner-circle">オンライン<br>予約</div>
  <div class="banner banner-wide">
    <svg width="34" height="34" viewBox="0 0 34 34" aria-hidden="true"><circle cx="17" cy="17" r="15" fill="none" stroke="#444" stroke-width="2"/><text x="17" y="23" text-anchor="middle" font-size="18" font-family="sans-serif" fill="#444">?</text></svg>
    よくあるご質問
  </div>
  <div class="banner banner-wide">
    <svg width="34" height="28" viewBox="0 0 34 28" aria-hidden="true"><rect x="2" y="2" width="30" height="24" fill="none" stroke="#444" stroke-width="2"/><path d="M2 2 L17 15 L32 2" fill="none" stroke="#444" stroke-width="2"/></svg>
    お問い合わせ
  </div>
  <div class="banner banner-dark">RECRUIT<small>採用情報</small></div>
  <div class="banner banner-wide">会社概要</div>
  <div class="banner banner-sns"><i></i>SNS</div>
</div>

<section class="section info">
  <div class="side-label"><span>INFO</span></div>
  <div class="section-body">
    <div class="info-cols">
      <div>
        <p class="info-name">Salon</p>
        <p class="info-addr">東京都中央区銀座3-8-14<br>ルミエ銀座ビル5階</p>
        <p class="info-tel">03-5000-4127</p>
        <p class="info-note">ご予約はお電話またはオンライン予約にて承ります。キャンセルの場合はご連絡ください。</p>
      </div>
      <div class="info-map" role="img" aria-label="Street map of the area around the salon in Ginza"></div>
      <table class="hours">
        <tr><th>営業時間</th><td></td></tr>
        <tr><th>月〜金</th><td>11:00 – 20:00</td></tr>
        <tr><th>土曜日</th><td>10:00 – 20:00</td></tr>
        <tr><th>日・祝日</th><td>10:00 – 19:00</td></tr>
        <tr><th>定休日</th><td>毎週火曜日</td></tr>
      </table>
    </div>
  </div>
</section>

<footer class="footer">
  <nav class="fnav">
    <span>HOME</span><span>INFORMATION/PRESS</span><span>STYLIST</span><span>CATALOG</span><span>ACCESS</span><span>PRICE</span><span>CONTACT</span><span>RECRUIT</span><span>RESERVATION/ご予約</span>
  </nav>
  <p class="copy">Copyright © 2014 SALON All Rights Reserved</p>
</footer>

</body>
</html>
```